Financial Planning Business needs a business card design

We need a business card design that is for a new financial planning business based in Australia. We provide financial planning advice such as retirement planning, wealth creation, asset protection.

Attached is the logo design. On the front side of the business card needs to incorporate the following:
- adviser name
- adviser title (ie Managing Director)
- address
- phone number
- email
- website address

Ideally it should also have the business name and logo

On the back of the card I would like this to be black in colour with the business name and logo

I have been advised the font is "Cinzel" (regular and bold)

Industry/Entity Type

Financial

Requirements
Must have
• Logo and business name

Format to have as follows:
Ben xxxxxxxx
Managing Director / Senior Financial Adviser
address
phone email
website

```html
<!DOCTYPE html>
<html lang="en">
<head>
<meta charset="utf-8">
<title>Meridian Wealth Planning – Business Card</title>
<link rel="stylesheet" href="https://fonts.googleapis.com/css2?family=Cinzel:wght@400;700&family=Open+Sans:wght@400&display=swap">
<style>
  :root {
    --brand-blue: #0a8fd0;
    --back-black: #151515;
    --back-black-deep: #050505;
    --card-white: #f7f7f7;
    --band-grey: #bcbcbc;
    --mark-grey: #8c8c8c;
    --ink: #2b2b2b;
    --rule: #333333;
    --backdrop: #e6e6e6;
    --on-dark: #ffffff;
  }
  * { box-sizing: border-box; margin: 0; padding: 0; }
  html, body { width: 1200px; height: 886px; overflow: hidden; }
  body {
    background: var(--backdrop);
    position: relative;
    font-family: "Open Sans", Arial, sans-serif;
  }
  .card {
    position: absolute;
    top: 288px;
    width: 540px;
    height: 310px;
    border-radius: 4px;
    box-shadow: 0 6px 18px rgba(0,0,0,0.18);
    overflow: hidden;
  }

  /* Back side */
  .card--back {
    left: 40px;
    background: linear-gradient(135deg, var(--back-black) 0%, var(--back-black-deep) 100%);
    display: flex;
    align-items: center;
    justify-content: center;
    gap: 18px;
  }
  .brand-square { width: 52px; height: 52px; flex: none; }
  .card--back .brand-square { background: var(--on-dark); }
  .brand-name {
    font-family: "Cinzel", Georgia, serif;
    font-weight: 400;
    line-height: 1;
  }
  .brand-name__main { display: block; font-size: 50px; letter-spacing: 1px; }
  .brand-name__sub { display: block; font-size: 21px; margin-top: 4px; letter-spacing: 1px; }
  .card--back .brand-name { color: var(--on-dark); }

  /* Front side */
  .card--front {
    left: 620px;
    background: var(--card-white);
  }
  .card--front .brand {
    position: absolute;
    left: 34px;
    top: 30px;
    display: flex;
    align-items: center;
    gap: 14px;
  }
  .card--front .brand-square { width: 42px; height: 42px; background: var(--mark-grey); }
  .card--front .brand-name { color: var(--brand-blue); }
  .card--front .brand-name__main { font-size: 36px; }
  .card--front .brand-name__sub { font-size: 15px; margin-top: 3px; }

  .adviser-line {
    position: absolute;
    left: 30px;
    right: 28px;
    top: 102px;
    display: flex;
    align-items: flex-start;
    gap: 10px;
  }
  .rule { height: 1px; background: var(--rule); margin-top: 16px; }
  .rule--left { flex: 1; }
  .rule--right { width: 50px; flex: none; }
  .adviser { flex: none; }
  .adviser__name {
    font-family: "Cinzel", Georgia, serif;
    font-size: 22px;
    line-height: 30px;
    color: var(--brand-blue);
    white-space: nowrap;
  }
  .adviser__title {
    font-size: 12px;
    color: var(--ink);
    margin-top: 2px;
  }

  .contact {
    position: absolute;
    left: 30px;
    top: 150px;
    list-style: none;
  }
  .contact__item {
    display: flex;
    align-items: center;
    gap: 12px;
    height: 21px;
    font-size: 11.5px;
    color: var(--ink);
    white-space: nowrap;
  }
  .contact__icon { width: 12px; height: 12px; flex: none; fill: var(--brand-blue); }

  .bottom-band { position: absolute; left: 0; bottom: 0; width: 540px; height: 26px; }
</style>
</head>
<body>

  <section class="card card--back" aria-label="Card back">
    <span class="brand-square"></span>
    <div class="brand-name">
      <span class="brand-name__main">Meridian</span>
      <span class="brand-name__sub">Wealth Planning</span>
    </div>
  </section>

  <section class="card card--front" aria-label="Card front">
    <div class="brand">
      <span class="brand-square"></span>
      <div class="brand-name">
        <span class="brand-name__main">Meridian</span>
        <span class="brand-name__sub">Wealth Planning</span>
      </div>
    </div>

    <div class="adviser-line">
      <span class="rule rule--left"></span>
      <div class="adviser">
        <p class="adviser__name">Liam Carter</p>
        <p class="adviser__title">Managing Director</p>
      </div>
      <span class="rule rule--right"></span>
    </div>

    <ul class="contact">
      <li class="contact__item">
        <svg class="contact__icon" viewBox="0 0 12 12"><path d="M2.5 0.5 L4.5 0.5 L5.2 3 L3.8 4 Q5 7 8 8.2 L9 6.8 L11.5 7.5 L11.5 9.5 Q11 11.5 9 11.5 Q1 10 0.5 3 Q0.5 1 2.5 0.5 Z"/></svg>
        <span>407-555-0142</span>
      </li>
      <li class="contact__item">
        <svg class="contact__icon" viewBox="0 0 12 12"><path d="M0.5 2.5 H11.5 V9.5 H0.5 Z M1 3 L6 6.8 L11 3" stroke="#fff" stroke-width="0.8"/></svg>
        <span>liamcarter@meridianwealthplanning.com</span>
      </li>
      <li class="contact__item">
        <svg class="contact__icon" viewBox="0 0 12 12"><circle cx="6" cy="6" r="5.5"/><path d="M0.5 6 H11.5 M6 0.5 V11.5 M1.5 3.2 H10.5 M1.5 8.8 H10.5" stroke="#fff" stroke-width="0.7" fill="none"/></svg>
        <span>www.meridianwealthplanning.com</span>
      </li>
      <li class="contact__item">
        <svg class="contact__icon" viewBox="0 0 12 12"><path d="M6 0.5 A4 4 0 0 1 10 4.5 C10 7.5 6 11.5 6 11.5 C6 11.5 2 7.5 2 4.5 A4 4 0 0 1 6 0.5 Z"/><circle cx="6" cy="4.5" r="1.5" fill="#fff"/></svg>
        <span>1200 Harbor View Rd. Suite 410 - Orlando, FL 32801</span>
      </li>
    </ul>

    <svg class="bottom-band" viewBox="0 0 540 26" preserveAspectRatio="none">
      <polygon points="0,0 340,0 322,26 0,26" fill="var(--brand-blue)"/>
      <polygon points="348,0 540,0 540,26 330,26" fill="var(--band-grey)"/>
    </svg>
  </section>

</body>
</html>
```